A r&b and house DJ needs a new Graphically pleasing and trendy website for fans and potential client

Want a new design for a dj website. This website wont be updated often so needs to look very graphically pleasing and just be a point of call where fans and potential clients can come and see information about the dj etc.

Needs to have short bio , social network links, and a enquiry button.

You can use some stock images for the moment as some professional images are going to be taken.

Others DJ websites:

https://www.djvornley.com/
http://www.pelkansoutar.com/
http://vomaro.com/
http://uletto.com/
http://www.dorianwelkby.co.uk/gb/home
http://www.fumbrelquix.com/
http://plinvaro.nl/

LOGO LINK IS HERE

https://www.filecrate-example.com/s/kq7wz2m9tnh4xa1/DJ_Vellum_logo.eps?dl=0

Target Market(s)

Fans and also prospective clients ( Nightclubs, Record Labels)

Industry/Entity Type

House

Font styles to use
Sans Serif

Requirements
Must have
• Small Bio, Social Network Links, Enquiry Button.
Nice to have
• Social network links

```html
<!DOCTYPE html>
<html lang="en">
<head>
<meta charset="utf-8">
<title>Velmora Sounds R &amp; B</title>
<link href="https://fonts.googleapis.com/css2?family=Open+Sans:wght@400;600;700;800&family=Arimo:wght@400&display=swap" rel="stylesheet">
<style>
:root{
  --bg:#141414;
  --header:#1b1b1b;
  --red:#d3111d;
  --maroon:#6a0221;
  --teal:#0f4946;
  --bar:#262626;
  --muted:#8c8c8c;
  --white:#ffffff;
  --ink:#151515;
}
*{margin:0;padding:0;box-sizing:border-box}
html,body{width:1200px;height:899px;overflow:hidden;background:var(--bg);font-family:"Open Sans",sans-serif}
.page{position:relative;width:1200px;height:899px}
.header{position:absolute;left:0;top:0;width:1200px;height:72px;background:var(--header)}
.brand{position:absolute;left:26px;top:21px;font-size:22px;font-weight:600;color:var(--red);display:flex;align-items:center;gap:8px;white-space:nowrap}
.brand-dot{width:10px;height:10px;border-radius:50%;background:var(--red)}
.nav{position:absolute;top:30px;left:0;font-size:11.5px;color:#a9a9a9}
.nav span{position:absolute;white-space:nowrap}
.search{position:absolute;left:876px;top:21px;width:30px;height:30px;border:1px solid #3a3a3a;border-radius:50%}
.drop{position:absolute;top:21px;height:30px;border:1px solid #3a3a3a;color:#a9a9a9;font-size:10px;line-height:28px;padding-left:12px}
.drop::after{content:"";position:absolute;right:11px;top:12px;border:4px solid transparent;border-top-color:#a9a9a9}
.hero{position:absolute;left:0;top:72px;width:642px;height:565px;background:radial-gradient(circle at 70% 30%,#6fb5ff 0%,#3a5fc8 25%,#5a2a8e 55%,#2a1a3a 100%)}
.hero-text{position:absolute;left:39px;top:110px}
.hero h1{font-weight:800;font-size:46px;line-height:48px;color:var(--white);white-space:nowrap}
.hero h2{font-weight:800;font-size:31px;line-height:40px;color:var(--white);white-space:nowrap}
.hero h3{font-weight:700;font-size:28.5px;line-height:29px;color:var(--ink);margin-top:10px;white-space:nowrap}
.btn{position:absolute;left:39px;top:313px;width:198px;height:48px;background:var(--red);color:var(--white);font-weight:700;font-size:16px;line-height:48px;text-align:center;border-radius:2px}
.arrows{position:absolute;left:578px;top:527px;display:flex;gap:1px}
.arrows div{width:27px;height:28px;background:var(--red)}
.grid{position:absolute;left:655px;top:84px;width:532px;height:534px}
.cell{position:absolute;width:260px;height:267px}
.card{padding:30px 10px 0 28px;color:var(--white)}
.card h4{font-size:17px;font-weight:600;line-height:24px}
.card p{font-family:"Arimo",sans-serif;font-size:10.2px;line-height:21.4px;margin-top:10px}
.more{font-family:"Arimo",sans-serif;font-size:11px;margin-top:6px;display:flex;align-items:center;gap:5px;padding-left:3px}
.more i{width:9px;height:9px;border-radius:50%;background:var(--white);display:inline-block}
.slider{position:absolute;left:655px;top:621px;width:532px;height:16px;background:var(--bar)}
.strip{position:absolute;left:0;top:649px;width:1200px;height:183px}
.tile{position:absolute;top:0;width:298px;height:183px}
.tag{position:absolute;left:0;top:138px;height:34px;width:185px;background:var(--red);clip-path:polygon(0 0,100% 0,94% 100%,0 100%);color:var(--white);font-weight:700;font-size:13px;line-height:34px;padding-left:11px;white-space:nowrap}
.footer{position:absolute;left:0;top:842px;width:1200px;height:57px;background:#1b1b1b;color:var(--muted);font-size:10.5px}
.footer .legal{position:absolute;left:26px;top:21px;white-space:nowrap}
.footer .social{position:absolute;left:740px;top:21px;display:flex;align-items:center;gap:19px;white-space:nowrap}
.footer .social i{width:10px;height:10px;border-radius:50%;background:#6f6f6f;display:inline-block}
</style>
</head>
<body>
<div class="page">
  <header class="header">
    <div class="brand"><span class="brand-dot"></span>Velmora Sounds R &amp; B</div>
    <nav class="nav">
      <span style="left:380px">NEWS</span><span style="left:457px">MUSIC</span><span style="left:537px">MEDIA</span>
      <span style="left:619px">SOCIAL</span><span style="left:703px">RADIO</span><span style="left:783px">FOUNDATION</span>
    </nav>
    <div class="search"><svg width="30" height="30" viewBox="0 0 30 30"><circle cx="14" cy="14" r="4" fill="none" stroke="#a9a9a9" stroke-width="1.5"/><line x1="17" y1="17" x2="20" y2="20" stroke="#a9a9a9" stroke-width="1.5"/></svg></div>
    <div class="drop" style="left:924px;width:124px">ENQUIRY</div>
    <div class="drop" style="left:1061px;width:124px">MEMBERS LOGIN</div>
  </header>

  <section class="hero" role="img" aria-label="DJ at turntables under blue and purple club lights">
    <div class="hero-text">
      <h1>WELCOME TO</h1>
      <h2>VELMORA SOUNDS R &amp; B</h2>
      <h3>LOREM IPSUM IS SIMPLY<br>DUMMY TEXT OF THE<br>PRINTING</h3>
    </div>
    <div class="btn">SOCIAL NETWORK</div>
    <div class="arrows">
      <div><svg width="27" height="28"><polyline points="16,8 10,14 16,20" fill="none" stroke="#fff" stroke-width="1.5"/></svg></div>
      <div><svg width="27" height="28"><polyline points="11,8 17,14 11,20" fill="none" stroke="#fff" stroke-width="1.5"/></svg></div>
    </div>
  </section>

  <section class="grid">
    <article class="cell card" style="left:0;top:0;background:var(--maroon)">
      <h4>LOREM IPSUM IS SIMPLY DUMMY TEXT OF THE PRINTING</h4>
      <p>Lorem Ipsum is simply dummy text of the printing and typesetting industry. Lorem Ipsum has been the industry's standard dummy text ever since the 1500s, when an unknown printer took a galley of type...</p>
      <div class="more">Read more <i></i></div>
    </article>
    <div class="cell" style="left:272px;top:0;background:linear-gradient(135deg,#c9b8ff,#7a3cc0 50%,#2a1440)" role="img" aria-label="DJ with headphones and glasses in violet light"></div>
    <div class="cell" style="left:0;top:267px;background:linear-gradient(135deg,#3a6ad0,#b0405a 45%,#5a2a20 100%)" role="img" aria-label="Two women dancing at a party"></div>
    <article class="cell card" style="left:272px;top:267px;background:var(--teal)">
      <h4>LOREM IPSUM IS SIMPLY DUMMY TEXT OF THE PRINTING</h4>
      <p>Lorem Ipsum is simply dummy text of the printing and typesetting industry. Lorem Ipsum has been the industry's standard dummy text ever since the 1500s, when an unknown printer took a galley of type...</p>
      <div class="more">Read more <i></i></div>
    </article>
  </section>
  <div class="slider">
    <svg width="532" height="16"><polyline points="14,4 10,8 14,12" fill="none" stroke="#888"/><rect x="262" y="5" width="2" height="6" fill="#888"/><rect x="266" y="5" width="2" height="6" fill="#888"/><polyline points="518,4 522,8 518,12" fill="none" stroke="#888"/></svg>
  </div>

  <section class="strip">
    <div class="tile" style="left:0;background:linear-gradient(135deg,#2a5a20,#3ccf3a 60%,#1a2a10)" role="img" aria-label="Crowd dancing in green club light"><div class="tag">LOREM IPSUM IS SIMPLY</div></div>
    <div class="tile" style="left:300px;background:linear-gradient(135deg,#0a1a50,#2a6ad0 55%,#0a1030)" role="img" aria-label="DJ performing on a stage in blue light"><div class="tag">LOREM IPSUM IS SIMPLY</div></div>
    <div class="tile" style="left:600px;background:linear-gradient(135deg,#2a2a30,#4a4a58 55%,#18181e)" role="img" aria-label="Turntables and mixer close up"><div class="tag">LOREM IPSUM IS SIMPLY</div></div>
    <div class="tile" style="left:901px;background:linear-gradient(135deg,#f0a020,#c84010 55%,#3a0a05)" role="img" aria-label="Concert crowd with raised hands in orange light"><div class="tag">LOREM IPSUM IS SIMPLY</div></div>
  </section>

  <footer class="footer">
    <div class="legal">© COPYRIGHT 2015, VELMORA SOUNDS R &amp; B. ALL RIGHTS RESERVED. &nbsp;| PRIVACY POLICY | TERMS &amp; CONDITIONS</div>
    <div class="social">CONNECT WITH OUR SOCIAL NETWORK : <i></i><i></i><i></i><i></i><i></i><i></i></div>
  </footer>
</div>
</body>
</html>
```